Banner Ad Design for Bannerly

We are an online upscale fashion private sales site that requires banners in the following sizes and dimensions (see below). For submission, you can just submit three variations (letterheard, skyscrapper and square). The rest can be submitted later on when your design is selected. All banners can have the same look and feel or different if you feel so. They are going to be used in Quorbix. So it's mandatory to abide by Quorbix guidelines (Reminder given below). I have attached two files for your use, one is the company's logo and the other is one couple picture that you could use in the banner - You dont have to use them, they are material for your thoughts.

Creative Direction of Ad:
* Simple and not overly crowded
* Has a call to action (Join us, etc)
* Attention grabbing and conforms to an upscale fashion retailer (Chic & Stylish)
* Uses at least one of our unique selling proposition texts
* Informative and promotes only a visitor who is interested to click

Unique Selling Proposition:
* Private sales in Morocco
* Upscale fashion brands at -70%
* Exclusively in Morocco

IMPORTANT: Please make the banner in English but after the winner is selected, I will need the banner in French (I will provide you with the appropriate translation).

Sizes: (MAX 50K or smaller)
1. Square 250 x250
2. Small Square 200 x 189
3. Leaderboard 728 x 79
4. Sky scrapper 160x600
4. Medium Rectangle 300 x 250
5. Large Rectangle 336 x 280

(After the successful award, please also adapt the banner to add the following sizes
6. Leaderboard 468 x 60
7. Skyscrapper 120 x 600)

Winner will send the files in .Gif, JPEG, & PSD. If you have any questions, please dont hesitate to ask.

======================================================
Quorbix Terms:
Ad images must be clear, recognizable, and relevant. Text appearing in the ad images must be legible. We reserve the right to disapprove low quality or blurry ad images.

Strobing, flashing backgrounds, or otherwise distracting ads are not allowed.
Your ads cannot mimic news articles and features. They may also not contain screenshots of Quorbix PlaceAds text ads or otherwise simulate an PlaceAds text ad in any way.
Ads cannot pretend to be a system or site warning.
Ads cannot mimic or resemble Pellucid, Orb, or Zent dialogue boxes, error message, etc.
Ads cannot have mock animated features or icons.
Ads can have an imaged button as long as the purpose of the message within the button is served or achieved through the landing page.
Specific for animated and display ad builder (template) ads:
Ads cannot have mock animated features or icons without the functionality working.

Target Market(s)

23-45 years white collard suburbans (Men & Women)

Industry/Entity Type

Fashion

Requirements
Must have
• Chic & Stylish Design.
It is not mandatory to use one of the logo file atatched but if you do not use it, please clearly display the site url (ELITE-CLUB.ma)
Nice to have
• The couple picture attached but not necesarily if you have better design. I have provided two logos version (one with white and the other with black background. Use the one that suits your design best).

```html
<!DOCTYPE html>
<html lang="en">
<head>
<meta charset="utf-8">
<title>Elite-club.ma banner set</title>
<link rel="stylesheet" href="https://fonts.googleapis.com/css2?family=Pinyon+Script&family=Arimo:wght@700&family=Gentium+Book+Plus&display=swap">
<style>
:root{
  --green-light:#a6d85a;
  --green:#6cb52b;
  --green-dark:#3f8a12;
  --ink:#1b1b1b;
  --white:#ffffff;
  --frame:#2a2a2a;
  --orange-light:#ffc94a;
  --orange:#f79a0c;
  --orange-dark:#e07a00;
  --button-text:#6f6f6f;
  --photo-a:#5a3a2c;
  --photo-b:#c9c3bb;
}
*{box-sizing:border-box;margin:0;padding:0}
html,body{width:1200px;height:1200px;overflow:hidden;background:var(--white)}
body{position:relative;font-family:"Gentium Book Plus",serif;color:var(--ink)}
.banner{position:absolute;border:1px solid var(--frame);overflow:hidden;background:var(--white)}
.script{font-family:"Pinyon Script",cursive;color:var(--white);text-shadow:1px 1px 2px rgba(0,0,0,.45)}
.bold{font-family:"Arimo",sans-serif;font-weight:700;color:var(--white);text-shadow:1px 2px 2px rgba(0,0,0,.55)}
.plain{font-family:"Arimo",sans-serif;color:var(--white)}
.header-green{background:linear-gradient(180deg,var(--green-light),var(--green) 55%,var(--green-dark))}
.photo{position:absolute;background:linear-gradient(160deg,var(--photo-a) 0%,#8a5a44 40%,var(--photo-b) 75%,#eeeae4 100%)}
.panel{position:absolute}
.panel svg{position:absolute;inset:0;width:100%;height:100%}
.text-block{position:absolute;text-align:center;line-height:1.1}
.join-button{position:absolute;display:block;text-decoration:none;color:var(--button-text);border-radius:12px;padding:4px;background:linear-gradient(180deg,#f2f2f2,#9a9a9a);box-shadow:0 2px 4px rgba(0,0,0,.35)}
.join-button .button-face{display:flex;flex-direction:column;align-items:center;justify-content:center;width:100%;height:100%;border-radius:9px;
  background:linear-gradient(180deg,var(--orange-light) 0%,var(--orange) 50%,var(--orange-dark) 100%);
  font-family:"Arimo",sans-serif;font-weight:700;color:var(--button-text);text-decoration:none;text-align:center;text-shadow:0 1px 0 rgba(255,255,255,.8);line-height:1.05}
.join-button .button-line{display:block}
.url{font-family:"Gentium Book Plus",serif}

/* leaderboard */
.leaderboard{left:86px;top:48px;width:1025px;height:124px;background:linear-gradient(90deg,#fff 0%,#fff 80%,#d4d4d4 100%)}
.leaderboard .brand-box{position:absolute;left:0;top:0;width:208px;height:100%;text-align:center;padding-top:4px}
.leaderboard .photo{left:208px;top:0;width:330px;height:100%}
.leaderboard .panel{left:510px;top:0;width:340px;height:100%}
.leaderboard .join-button{left:878px;top:10px;width:102px;height:104px;font-size:30px}

/* square */
.square{left:88px;top:264px;width:353px;height:353px}
.square .brand-box{position:absolute;left:0;top:0;width:100%;height:88px;text-align:center;padding-top:4px}
.square .photo{left:0;top:88px;width:100%;height:125px}
.square .panel{left:0;top:185px;width:100%;height:135px}
.square .url-strip{position:absolute;left:0;bottom:0;width:100%;height:34px;text-align:center;font-size:24px;line-height:34px}
.square .join-button{left:122px;top:196px;width:106px;height:108px;font-size:32px}

/* skyscraper */
.skyscraper{left:884px;top:227px;width:223px;height:844px;background:linear-gradient(180deg,#fff 70%,#e3e3e3 100%)}
.skyscraper .brand-box{position:absolute;left:0;top:0;width:100%;height:145px;text-align:center;padding-top:8px}
.skyscraper .photo{left:0;top:145px;width:100%;height:300px}
.skyscraper .panel{left:0;top:430px;width:100%;height:232px}
.skyscraper .url{position:absolute;left:0;top:672px;width:100%;text-align:center;font-size:28px}
.skyscraper .join-button{left:56px;top:722px;width:106px;height:106px;font-size:32px}
</style>
</head>
<body>

<section class="banner leaderboard" aria-label="Leaderboard banner">
  <div class="brand-box header-green">
    <div class="script" style="font-size:32px;line-height:1">Private Sales</div>
    <div class="plain" style="font-size:24px;line-height:1.1">in</div>
    <div class="bold" style="font-size:36px;line-height:1.05">Morocco</div>
  </div>
  <div class="photo" role="img" aria-label="Photo of a stylish couple in sunglasses with a vintage car"></div>
  <div class="panel">
    <svg viewBox="0 0 340 124" preserveAspectRatio="none" aria-hidden="true">
      <defs><radialGradient id="lb-glow" cx="0.4" cy="0.6" r="0.7"><stop offset="0" stop-color="#e4f6c6"/><stop offset="0.55" stop-color="#94cc4c"/><stop offset="1" stop-color="#4f9a1a"/></radialGradient></defs>
      <path d="M30 0 H300 Q345 62 300 124 H30 Q0 62 30 0 Z" fill="url(#lb-glow)" stroke="#fff" stroke-width="4"/>
    </svg>
    <div class="text-block" style="left:30px;top:4px;width:280px;font-size:30px">Upscale Fashion</div>
    <div class="text-block" style="left:30px;top:42px;width:280px;font-size:28px">Brands&ensp;&ensp;At - 70%</div>
    <div class="text-block url" style="left:30px;top:84px;width:280px;font-size:23px;color:var(--white);text-shadow:1px 1px 1px rgba(0,0,0,.4)">Elite-club.ma</div>
  </div>
  <a class="join-button" href="#"><span class="button-face"><span class="button-line">Join</span><span class="button-line">Us</span></span></a>
</section>

<section class="banner square" aria-label="Square banner">
  <div class="brand-box header-green">
    <div><span class="script" style="font-size:34px">Private Sales</span> <span class="plain" style="font-size:26px">in</span></div>
    <div class="bold" style="font-size:36px;line-height:1">Morocco</div>
  </div>
  <div class="photo" role="img" aria-label="Photo of a stylish couple in sunglasses with a vintage car"></div>
  <div class="panel">
    <svg viewBox="0 0 353 135" preserveAspectRatio="none" aria-hidden="true">
      <defs><radialGradient id="sq-glow" cx="0.5" cy="0.6" r="0.7"><stop offset="0" stop-color="#d8f0b0"/><stop offset="0.5" stop-color="#8cc644"/><stop offset="1" stop-color="#3f8a12"/></radialGradient></defs>
      <path d="M0 20 Q176 -8 353 20 V135 H0 Z" fill="url(#sq-glow)" stroke="#fff" stroke-width="4"/>
    </svg>
    <div class="text-block" style="left:6px;top:30px;width:108px;font-size:23px">Upscale<br>Fashion<br>Brands</div>
    <div class="text-block" style="left:236px;top:26px;width:116px;color:var(--white);text-shadow:1px 1px 2px rgba(0,0,0,.4)"><div style="font-size:22px">At</div><div style="font-size:44px">70%</div></div>
  </div>
  <div class="url-strip url">Elite-club.ma</div>
  <a class="join-button" href="#"><span class="button-face"><span class="button-line">Join</span><span class="button-line">Us</span></span></a>
</section>

<section class="banner skyscraper" aria-label="Skyscraper banner">
  <div class="brand-box header-green">
    <div class="script" style="font-size:34px;line-height:1.1">Private Sales</div>
    <div class="plain" style="font-size:26px;line-height:1.1">in</div>
    <div class="bold" style="font-size:36px;line-height:1.2">Morocco</div>
  </div>
  <div class="photo" role="img" aria-label="Photo of a stylish couple in sunglasses with a vintage car"></div>
  <div class="panel">
    <svg viewBox="0 0 223 232" preserveAspectRatio="none" aria-hidden="true">
      <defs><radialGradient id="sk-glow" cx="0.5" cy="0.55" r="0.75"><stop offset="0" stop-color="#d8f0b0"/><stop offset="0.5" stop-color="#8cc644"/><stop offset="1" stop-color="#3f8a12"/></radialGradient></defs>
      <path d="M0 22 Q111 -6 223 22 V232 H0 Z" fill="url(#sk-glow)" stroke="#fff" stroke-width="4"/>
    </svg>
    <div class="text-block" style="left:0;top:32px;width:100%;font-size:35px;line-height:1.28">Upscale<br>Fashion<br>Brands<br>At - 70%</div>
  </div>
  <div class="url">Elite-club.ma</div>
  <a class="join-button" href="#"><span class="button-face"><span class="button-line">Join</span><span class="button-line">Us</span></span></a>
</section>

</body>
</html>
```